依頼詳細
●デザインの要望
・少し温かみ、やわらかさのあるデザイン(まるっこすぎない)
※参考例:poruくらいのやわらかさ
・そのほかの色については特に指定なし(現在の青は入れなくてOKです)
⇒カラフルにするかどうかもデザインの中で考えて頂いて結構です
・現在のアプリにある下記のボタンを全て実装する
※投稿ボタン、画面更新ボタン、履歴ボタン、オプションボタン、カテゴリ選択ボタン の5個
・投稿が表示されるマス目は正方形だけでなく長方形等もまぜてほしい
※現在は正方形オンリーですが、縦に2個くっつけたものや横に2個くっつけたものが入ってきたりするデザイン
⇒アプリ:Tiledeck の記事一覧画面のようなイメージ
・zelvonなのでzvos7のフラットなイメージ(がっつり立体的にはしてほしくないです)

●納品物
PSDファイル1個(zelvonで使用する倍のサイズの 1920x1280 くらいで作ってください)
可能であればレイヤーのあるPNGファイル(可能であればで結構です)

サイトURL
https://apps.trovenlo.jp/jp/app/id518203764?mt=8
ページ数
1ページ
希望イメージ
シンプル 複雑
単色 カラフル
暗い 明るい
日常 高級
遊び心 厳粛
未来的 伝統的
女性的 男性的
希望する色
小豆色や薄い茶色等温かみのある色全般
納品ファイル
• フォトショップ形式 (.psd)
• PNG形式 (.png)
補足説明
■ 選んだ理由

やわらかいテイストでかつ既存の青をさし色に入れて頂けたこと、
またプラスアルファとしてスプラッシュスクリーンをご提示いただけたため、
より実装後のアプリのイメージがわくことができました。

■ 提案者全員のお礼・コメント

たくさんのご提案ありがとうございました。
特にUIそのものまで提案して頂けたりと非常にこちらとしても勉強になる案件となりました。

上部のバーのデザインや、吹き出し型のデザイン、カラフル、マット等
かなり悩ませていただきました。
最終的にはより女性的で、かつ落ち着いている
という部分を基準に選ぶことにしました。

本アプリは今後もどんどん改良を加える予定のため、
また機会が有りましたら是非宜しくお願い致します。

```html
<!DOCTYPE html>
<html lang="ja">
<head>
<meta charset="utf-8">
<title>Tile Board</title>
<link rel="stylesheet" href="https://fonts.googleapis.com/css2?family=Noto+Sans+JP:wght@400;500&display=swap">
<style>
  :root {
    --mauve: #7d3a58;
    --pink: #e5607c;
    --salmon: #f0a294;
    --orange: #ef8a52;
    --berry: #a8467c;
    --peach: #f8c58f;
    --paper: #ffffff;
    --ink: #6b4450;
    --bar: #7a2b45;
    --light: #ffffff;
    --gap: #f4ecee;
  }
  * { box-sizing: border-box; margin: 0; padding: 0; }
  html, body { width: 800px; height: 1200px; overflow: hidden; background: var(--gap); }
  body { font-family: "Noto Sans JP", sans-serif; position: relative; }
  .board { position: absolute; left: 0; top: 0; width: 800px; height: 1053px; overflow: hidden; }
  .tile {
    position: absolute; overflow: hidden;
    color: var(--light); font-size: 25px; line-height: 1.42;
    padding: 26px 22px; letter-spacing: 0.02em;
    border: 1px solid rgba(255,255,255,0.35);
  }
  .tile--light { background: var(--paper); color: var(--ink); }
  .tile--mauve { background: var(--mauve); }
  .tile--pink { background: var(--pink); }
  .tile--salmon { background: var(--salmon); }
  .tile--orange { background: var(--orange); }
  .tile--berry { background: var(--berry); }
  .tile--peach { background: var(--peach); }
  .tile--center { display: flex; align-items: center; }
  .post { width: 330px; }
  .post--cut-left { margin-left: -150px; text-align: right; width: 260px; }
  .post--cut-right { width: 330px; }
  .toolbar {
    position: absolute; left: 0; top: 1053px; width: 800px; height: 147px;
    background: var(--bar); display: flex; align-items: center;
    justify-content: space-around; padding: 0 20px;
  }
  .tool { width: 70px; height: 70px; display: flex; align-items: center; justify-content: center; color: var(--light); }
  .tool svg { width: 62px; height: 62px; }
  .tool__label { font-size: 28px; font-weight: 500; color: var(--light); }
</style>
</head>
<body>
<main class="board">
  <article class="tile tile--mauve" style="left:0;top:0;width:133px;height:240px">
    <p class="post post--cut-left">なんて言ったら、ドキドキしちゃうんじゃうよー！</p>
  </article>
  <article class="tile tile--light" style="left:133px;top:0;width:267px;height:507px">
    <p class="post" style="width:225px">ほぼTALKO上でしか話してなかった元カレが、かっこ良くなってた。友達に戻ろうって言ったけどなかなかできない。かっこよくなってて、また気持ちがゆれ始めたけど、そんなの自分勝手すぎな。</p>
  </article>
  <article class="tile tile--salmon" style="left:400px;top:0;width:267px;height:240px">
    <p class="post" style="width:225px">友達、出来るかな</p>
  </article>
  <article class="tile tile--pink" style="left:667px;top:0;width:133px;height:507px">
    <p class="post post--cut-right">あーやだ…もうすぐ返事が返ってこない。何か良いことはないかな。そんな訳でもないし相談したら、みんなからは優しい評価をもらわなきゃいけない。</p>
  </article>
  <article class="tile tile--pink tile--center" style="left:0;top:240px;width:133px;height:267px">
    <p class="post post--cut-left">帰って来ない</p>
  </article>
  <article class="tile tile--orange" style="left:400px;top:240px;width:267px;height:267px">
    <p class="post" style="width:225px">新しいお家にも来てくれますか？そしてあなたの新しいお家にも遊びに行ってもいいですか</p>
  </article>
  <article class="tile tile--pink tile--center" style="left:0;top:507px;width:400px;height:266px">
    <p class="post post--cut-left" style="width:500px;text-align:left;margin-left:-120px">いつもあなたと一緒でした。でも今はもお…あなたはいない。あなたの声が聴きたい。</p>
  </article>
  <article class="tile tile--mauve tile--center" style="left:400px;top:507px;width:267px;height:266px">
    <p class="post" style="width:225px">片思い楽しい。</p>
  </article>
  <article class="tile tile--pink tile--center" style="left:667px;top:507px;width:133px;height:266px">
    <p class="post post--cut-right">いっしょにいるのに寂しい</p>
  </article>
  <article class="tile tile--light tile--center" style="left:0;top:773px;width:133px;height:280px">
    <p class="post post--cut-left">あなたのうたの主人公だったかな</p>
  </article>
  <article class="tile tile--berry tile--center" style="left:133px;top:773px;width:267px;height:280px">
    <p class="post" style="width:225px">嫉妬しちゃうよ。なんでだろ。</p>
  </article>
  <article class="tile tile--peach tile--center" style="left:400px;top:773px;width:267px;height:280px">
    <p class="post" style="width:225px">あなた以上なんているわけないのに。</p>
  </article>
  <article class="tile tile--pink tile--center" style="left:667px;top:773px;width:133px;height:280px">
    <p class="post post--cut-right">つきあって一年。頭をさげてください。だけど悩みます。距離が遠い。</p>
  </article>
</main>

<nav class="toolbar">
  <span class="tool" aria-label="投稿">
    <svg viewBox="0 0 32 32" fill="none" stroke="currentColor" stroke-width="3" stroke-linejoin="round">
      <path d="M6 26l2-7L21 6l5 5-13 13z"/><path d="M18 9l5 5"/>
    </svg>
  </span>
  <span class="tool" aria-label="更新">
    <svg viewBox="0 0 32 32" fill="none" stroke="currentColor" stroke-width="3.4" stroke-linecap="round">
      <path d="M9 9a10 10 0 1 0 7-3"/><path d="M16 2l4 4-4 4" stroke-linejoin="round"/>
    </svg>
  </span>
  <span class="tool" aria-label="履歴">
    <svg viewBox="0 0 32 32">
      <rect x="6" y="5" width="20" height="24" rx="2" fill="currentColor"/>
      <rect x="11" y="3" width="10" height="5" rx="1" fill="var(--bar)" stroke="currentColor" stroke-width="2"/>
      <path d="M10 14h12M10 19h12M10 24h8" stroke="var(--bar)" stroke-width="2"/>
    </svg>
  </span>
  <span class="tool" aria-label="オプション">
    <svg viewBox="0 0 32 32">
      <g fill="currentColor">
        <circle cx="16" cy="16" r="9"/>
        <rect x="13.5" y="3" width="5" height="26" rx="1"/>
        <rect x="13.5" y="3" width="5" height="26" rx="1" transform="rotate(45 16 16)"/>
        <rect x="13.5" y="3" width="5" height="26" rx="1" transform="rotate(90 16 16)"/>
        <rect x="13.5" y="3" width="5" height="26" rx="1" transform="rotate(135 16 16)"/>
      </g>
      <circle cx="16" cy="16" r="4" fill="var(--bar)"/>
    </svg>
  </span>
  <span class="tool"><span class="tool__label">全体</span></span>
</nav>
</body>
</html>
```